Strength and Conditioning Business needs a logo design

We need a logo design for a fitness company based in South Carolina called "K9R Athletic Performance". We are a group of Strength and Conditioning Coaches that work with youth, high school, collegiate, and professional athletes. We also train general population clients that are looking to improve their overall fitness. Our primary mission is to make sure our athletes are able to gain the greatest benefits from training that will allow them to excel in their sport. We use heavy chains, kettle bells, resistance bands, dumbbells, prowlers (sleds), and multi-functional machines for training. We have a dynamic and collaborative approach that utilizes high-intensity intervals combined with speed, power, agility, and strength training.

Industry/Entity Type

Fitness

Contact Information for Business Card

K9R Athletic Performance
Lorenzo Pike, MS, CSCS, FMSC
Director of Sports Performance
Columbia, SC
Phone: (803) 517-3084
Email: k9rathleticperformance@mailbox-example.com
Instagram: iron_trainer_v

Font styles to use
Sans Serif

Colors
9bcb3c
ffffff
000000
474747
ec1f27
7f7f7f
0456a4

Requirements
Must have
• I would like to have a black card with either lime green or bold blue accents along with white and silver. On the back, I would like the name 'K9R Athletic Performance' with a subheading that says, 'Strength and Conditioning.'
Nice to have
• I really like the designs of the cards I uploaded. For the logo, something clean, bold, and eye-catching would be great.
Should not have
• I do not want a logo that will make it difficult to read.

```html
<!DOCTYPE html>
<html lang="en">
<head>
<meta charset="utf-8">
<title>K9R Athletic Performance — Business Card</title>
<link rel="stylesheet" href="https://fonts.googleapis.com/css2?family=Oswald:wght@400;500;600&family=Montserrat:wght@500&display=swap">
<style>
  :root {
    --lime: #9bcb3c;
    --white: #ffffff;
    --card: #1e1e1e;
    --silver: #d9d9d9;
    --stage: #8a8a8a;
  }
  * { box-sizing: border-box; margin: 0; padding: 0; }
  html, body { width: 1200px; height: 900px; overflow: hidden; }
  body {
    background: var(--stage);
    display: flex;
    flex-direction: column;
    align-items: center;
    justify-content: center;
    gap: 40px;
    font-family: "Oswald", sans-serif;
  }
  .card {
    width: 660px;
    height: 377px;
    background: var(--card);
    position: relative;
    color: var(--white);
  }
  /* contact side */
  .brand-small {
    position: absolute;
    top: 38px; left: 0; right: 0;
    text-align: center;
  }
  .brand-small .brand-name {
    font-weight: 600;
    font-size: 30px;
    letter-spacing: 1px;
    text-transform: uppercase;
    color: var(--white);
    line-height: 1;
  }
  .tagline {
    display: flex;
    align-items: center;
    justify-content: center;
    gap: 8px;
    font-family: "Montserrat", sans-serif;
    font-weight: 500;
    color: var(--lime);
    text-transform: uppercase;
  }
  .tagline::before, .tagline::after {
    content: "";
    height: 1px;
    background: var(--lime);
  }
  .brand-small .tagline { font-size: 8px; margin-top: 8px; letter-spacing: 0.5px; }
  .brand-small .tagline::before, .brand-small .tagline::after { width: 36px; }

  .details {
    position: absolute;
    top: 190px; left: 40px; right: 24px;
    display: flex;
    align-items: stretch;
  }
  .person {
    width: 230px;
    text-align: right;
    padding-right: 22px;
    border-right: 2px solid var(--lime);
    font-size: 17px;
    line-height: 1.35;
  }
  .person .person-name {
    color: var(--lime);
    font-size: 25px;
    font-weight: 500;
    text-transform: uppercase;
    line-height: 1.15;
  }
  .contact-list {
    list-style: none;
    padding-left: 20px;
    display: flex;
    flex-direction: column;
    justify-content: center;
    gap: 10px;
    font-size: 16px;
  }
  .contact-list li { display: flex; align-items: center; gap: 10px; white-space: nowrap; }
  .contact-icon {
    width: 24px; height: 24px;
    border-radius: 50%;
    background: var(--lime);
    flex-shrink: 0;
    display: flex; align-items: center; justify-content: center;
  }
  .contact-email { font-size: 14px; }

  /* logo side */
  .brand-large {
    position: absolute;
    inset: 0;
    display: flex;
    flex-direction: column;
    align-items: center;
    justify-content: center;
  }
  .brand-large .brand-name {
    font-weight: 600;
    font-size: 58px;
    letter-spacing: 1px;
    text-transform: uppercase;
    color: var(--white);
    line-height: 1.05;
    text-align: center;
  }
  .brand-large .tagline { font-size: 17px; margin-top: 18px; letter-spacing: 1px; }
  .brand-large .tagline::before, .brand-large .tagline::after { width: 60px; }
</style>
</head>
<body>
  <section class="card card-contact">
    <div class="brand-small">
      <div class="brand-name">K9R Athletic Performance</div>
      <div class="tagline">Strength and Conditioning</div>
    </div>
    <div class="details">
      <div class="person">
        <div class="person-name">Lorenzo Pike</div>
        <div>MS, CSCS, FMSC</div>
        <div>Director of Sports Performance</div>
        <div>Columbia, SC</div>
      </div>
      <ul class="contact-list">
        <li>
          <span class="contact-icon">
            <svg width="14" height="14" viewBox="0 0 24 24"><path fill="#1e1e1e" d="M6.6 10.8a15 15 0 0 0 6.6 6.6l2.2-2.2c.3-.3.7-.4 1-.2 1.1.4 2.3.6 3.6.6.6 0 1 .4 1 1V20c0 .6-.4 1-1 1A17 17 0 0 1 3 4c0-.6.4-1 1-1h3.5c.6 0 1 .4 1 1 0 1.3.2 2.5.6 3.6.1.3 0 .7-.2 1z"/></svg>
          </span>
          (803) 517-3084
        </li>
        <li>
          <span class="contact-icon">
            <svg width="14" height="14" viewBox="0 0 24 24"><rect x="3" y="6" width="18" height="12" fill="none" stroke="#1e1e1e" stroke-width="2"/><path d="M3 6l9 7 9-7" fill="none" stroke="#1e1e1e" stroke-width="2"/></svg>
          </span>
          <span class="contact-email">k9rathleticperformance@mailbox-example.com</span>
        </li>
        <li>
          <span class="contact-icon"></span>
          iron_trainer_v
        </li>
      </ul>
    </div>
  </section>

  <section class="card card-brand">
    <div class="brand-large">
      <div class="brand-name">K9R Athletic Performance</div>
      <div class="tagline">Strength and Conditioning</div>
    </div>
  </section>
</body>
</html>
```